New IT Consulting Company website - name is Zorvel Consulting

Seeking a new IT Consulting company website in Wordpress, some IT recruitment based skills, about us, services, we have all the content and wireframe details. We then want to build it in Divi ideally

Target Market(s)

IT Consulting companies and also staff augmentation needs

Industry/Entity Type

It Professional

Colors
0355a3

Requirements
Must have
• Home Page,
• Banner (Slider) - What we do
• Banner 2 - Companies / Talent we deal with (Quellbyte, Fendra, TQR, Lumo, Gravelonix etc)
• Our 3 key areas being:
• a) Integration Consulting and Staff Augmentation
• b) Software Development
• c) Data Consulting and Staff Augmentation
• About Data landing page
• About Integration landing page
• Media (news/blog)
• Contact Us
• Then About us - What we Do, How we do it, our values
• Our Solutions Page - Clients landing Page, Candidates landing Page
• Case Studies page
• Blog
• Contact Us
Nice to have
• NA
Should not have
• NA

```html
<!DOCTYPE html>
<html lang="en">
<head>
<meta charset="utf-8">
<title>Zorvel Consulting – Contact Us</title>
<link rel="stylesheet" href="https://fonts.googleapis.com/css2?family=Open+Sans:wght@400;600;700;800&display=swap">
<style>
  :root{
    --blue:#1d6ff2;
    --blue-dark:#0355a3;
    --green:#12c99b;
    --navy:#1e2838;
    --ink:#2b2f36;
    --muted:#8a9099;
    --line:#e3e6ea;
    --field:#f4f5f7;
    --white:#ffffff;
  }
  *{box-sizing:border-box;margin:0;padding:0}
  html,body{width:756px;height:1200px;overflow:hidden}
  body{font-family:"Open Sans",Arial,sans-serif;color:var(--ink);background:var(--white);position:relative}

  .hero{position:absolute;left:0;top:0;width:756px;height:205px;background:linear-gradient(180deg,#1f72f4,#1a66e6)}
  .nav{position:absolute;top:18px;left:55px;right:55px;display:flex;align-items:center;justify-content:space-between}
  .brand{color:var(--white);font-weight:700;font-size:20px}
  .menu{display:flex;align-items:center;gap:20px;list-style:none}
  .menu li{color:var(--white);font-size:10px;font-weight:600}
  .menu .cta{background:var(--green);padding:7px 11px;border-radius:2px;font-size:11px}
  .hero-title{position:absolute;top:72px;width:100%;text-align:center;color:var(--white);font-size:38px;font-weight:700}
  .crumbs{position:absolute;top:118px;width:100%;text-align:center;color:var(--white);font-size:10px;display:flex;justify-content:center;align-items:center;gap:6px}

  .cards{position:absolute;top:255px;left:112px;display:flex;gap:45px}
  .card{width:147px;height:130px;background:var(--white);box-shadow:0 3px 16px rgba(0,0,0,.12);text-align:center;padding-top:22px}
  .icon{width:34px;height:34px;border-radius:50%;margin:0 auto 12px;display:flex;align-items:center;justify-content:center}
  .icon.blue{background:#e3eefe}.icon.green{background:#dcf7ee}.icon.grey{background:#ececec}
  .card h3{font-size:12px;font-weight:700;margin-bottom:4px}
  .card p{font-size:7px;color:var(--muted);line-height:1.5;padding:0 16px}

  .section-title{position:absolute;top:442px;width:100%;text-align:center;font-size:26px;font-weight:600;letter-spacing:.5px;color:#2f3237}
  .title-rule{position:absolute;top:480px;left:352px;width:52px;height:4px;background:var(--green)}
  .section-sub{position:absolute;top:496px;width:100%;text-align:center;font-size:9px;color:var(--muted)}

  .form{position:absolute;top:540px;left:76px;width:604px}
  .row{display:flex;gap:14px;margin-bottom:14px}
  .field{flex:1;height:34px;background:var(--field);border:1px solid var(--line);font-size:8px;color:var(--muted);padding:11px 10px}
  .field.message{height:82px}
  .submit{display:block;margin:16px auto 0;width:76px;height:28px;background:var(--green);color:var(--white);font-size:10px;font-weight:700;border:none;border-radius:2px;font-family:inherit}

  .band{position:absolute;left:0;top:0}
  .join-title{position:absolute;top:836px;width:100%;text-align:center;color:var(--white);font-size:25px;font-weight:700}
  .join-text{position:absolute;top:880px;width:100%;text-align:center;color:#c4c9d2;font-size:9px;line-height:1.5}
  .join-btn{position:absolute;top:916px;left:330px;width:96px;height:28px;background:var(--green);color:var(--white);font-size:10px;font-weight:700;border-radius:2px;text-align:center;line-height:28px}

  .footer{position:absolute;top:983px;left:55px;right:40px;display:flex;color:var(--white)}
  .col h4{font-size:13px;font-weight:700;margin-bottom:10px}
  .col.about{width:260px}
  .col.about h4{font-size:22px;margin-bottom:12px}
  .col.about p{font-size:7px;line-height:1.6;color:#c4c9d2;width:205px}
  .social{display:flex;gap:8px;margin-top:12px}
  .social span{width:17px;height:17px;border-radius:50%;background:#3a4558}
  .col ul{list-style:none}
  .col li{font-size:9px;line-height:1.75;color:#e6e8ec}
  .col.links{width:108px}.col.services{width:122px}.col.contact{width:170px}
  .contact li{display:flex;gap:6px;line-height:1.5;margin-bottom:5px}
  .contact b{font-weight:700}
  .contact .map{color:var(--green);font-weight:700}
  .bottom-rule{position:absolute;top:1160px;left:40px;right:40px;height:1px;background:#3a4558}
  .bottom{position:absolute;top:1172px;left:55px;right:40px;display:flex;justify-content:space-between;color:#c4c9d2;font-size:8px}
  .bottom nav{display:flex;gap:22px}
</style>
</head>
<body>
  <header class="hero">
    <div class="nav">
      <div class="brand">Zorvel Consulting</div>
      <ul class="menu">
        <li>Home</li><li>About Us</li><li>Our Solutions</li><li>Testimonials</li><li>Case Studies</li><li>Blog</li><li class="cta">Contact Us</li>
      </ul>
    </div>
    <h1 class="hero-title">Contact Us</h1>
    <div class="crumbs">
      <svg width="10" height="9" viewBox="0 0 10 9"><path d="M5 0 10 4.5H8.5V9H6V6H4V9H1.5V4.5H0Z" fill="#fff"/></svg>
      <span>Home</span><span>|</span><span>Contact</span>
    </div>
  </header>

  <section class="cards">
    <div class="card">
      <div class="icon blue"><svg width="14" height="18" viewBox="0 0 14 18"><path d="M7 0C3 0 0 3 0 7c0 5 7 11 7 11s7-6 7-11c0-4-3-7-7-7z" fill="#1d6ff2"/><circle cx="7" cy="7" r="2.6" fill="#fff"/></svg></div>
      <h3>Office Address</h3>
      <p>Level 8, 24 Marlow Street, Northgate, 2041 (Map)</p>
    </div>
    <div class="card">
      <div class="icon green"><svg width="16" height="16" viewBox="0 0 16 16"><path d="M3 1l3 3-2 2c1 2 3 4 6 6l2-2 3 3-2 2C7 15 1 9 1 3z" fill="#12c99b"/></svg></div>
      <h3>Phone</h3>
      <p>02 5550 0142<br>Email Us</p>
    </div>
    <div class="card">
      <div class="icon grey"><svg width="16" height="16" viewBox="0 0 16 16"><circle cx="8" cy="8" r="7" fill="none" stroke="#555" stroke-width="1.4"/><path d="M1 8h14M8 1c-3 4-3 10 0 14M8 1c3 4 3 10 0 14" fill="none" stroke="#555" stroke-width="1.2"/></svg></div>
      <h3>Web</h3>
      <p>www.zorvelconsulting.example</p>
    </div>
  </section>

  <h2 class="section-title">SEND A MESSAGE</h2>
  <div class="title-rule"></div>
  <p class="section-sub">Interested in driving growth? Have a general question? We're just an email away.</p>

  <form class="form">
    <div class="row"><div class="field">Name</div><div class="field">Email Address</div></div>
    <div class="row"><div class="field message">Message</div></div>
    <button class="submit" type="button">Submit</button>
  </form>

  <svg class="band" width="756" height="1200" viewBox="0 0 756 1200" aria-hidden="true">
    <polygon points="0,828 756,758 756,1200 0,1200" fill="#1e2838"/>
  </svg>

  <h2 class="join-title">Be A Part Of IT Consulting</h2>
  <p class="join-text">It is a long established fact that a reader will be distracted by the readable content of a<br>page when looking at its layout.</p>
  <div class="join-btn">Join Us Today</div>

  <footer class="footer">
    <div class="col about">
      <h4>Zorvel Consulting</h4>
      <p>Our focus is helping you find skilled IT people and practical solutions, with a team that listens first, plans with care and stays on hand from the first brief to long after the work goes live.</p>
      <div class="social"><span></span><span></span><span></span><span></span></div>
    </div>
    <div class="col links">
      <h4>Quick Links</h4>
      <ul><li>Home</li><li>About Us</li><li>Services</li><li>Portfolio</li><li>Contact</li></ul>
    </div>
    <div class="col services">
      <h4>Services</h4>
      <ul><li>App Development</li><li>Software Support</li><li>Data Management</li><li>Network Security</li><li>Cloud Computing</li></ul>
    </div>
    <div class="col contact">
      <h4>Contact</h4>
      <ul>
        <li><span><b>location:</b> Level 8, 24 Marlow Street, Northgate, 2041 <span class="map">(Map)</span></span></li>
        <li><span><b>Email:</b> Email Us</span></li>
        <li><span><b>Phone:</b> 02 5550 0142</span></li>
        <li><span><b>Web:</b> www.zorvelconsulting.example</span></li>
        <li><span class="map">View Map</span></li>
      </ul>
    </div>
  </footer>
  <div class="bottom-rule"></div>
  <div class="bottom">
    <span>© Copyright 2019 - All rights reserved</span>
    <nav><span>Terms &amp; Condition</span><span>Privacy Policy</span></nav>
  </div>
</body>
</html>
```